We are looking for a clean new looking business card.

We would like a new, clean, and modern type business card with our updated contact information. We are a small a plumbing and heating and gasfitting company who offer 24 hr emergency service as well.
We feel our logo looks best on a white background.
Our current cards are outdated, both the design and the information.

Industry/Entity Type

Plumbing and heating

Contact Information for Business Card

Logo, Name, Title, Phone#, Email, Website, "24/7 Emergency Service"

Colors
0054AA
0677BA
7BADD7
CADEEF
E8F1F8

```html
<!DOCTYPE html>
<html lang="en">
<head>
<meta charset="UTF-8">
<title>harborline — Business Card</title>
<link href="https://fonts.googleapis.com/css2?family=Montserrat:wght@400;500;600;700;800&display=swap" rel="stylesheet">
<style>
  :root {
    --navy: #0054AA;
    --blue: #0677BA;
    --sky: #7BADD7;
    --mist: #CADEEF;
    --ice: #E8F1F8;
    --ink: #2b2b2b;
    --grey: #555b61;
    --white: #ffffff;
    --stage: #eef1f4;
  }
  * { box-sizing: border-box; margin: 0; padding: 0; }
  html, body { width: 1200px; height: 800px; overflow: hidden; }
  body {
    background: var(--stage);
    font-family: "Montserrat", sans-serif;
    display: flex;
    align-items: center;
    justify-content: center;
    gap: 48px;
  }
  .card {
    position: relative;
    width: 525px;
    height: 300px;
    border-radius: 18px;
    overflow: hidden;
    box-shadow: 0 10px 30px rgba(0, 40, 80, 0.15);
  }

  /* Front */
  .card--front { background: var(--white); }
  .card__accent {
    position: absolute;
    left: 0; bottom: 0;
    width: 44%;
    height: 9px;
    background: var(--blue);
  }
  .card__halo {
    position: absolute;
    right: -40px; top: 30px;
    width: 230px; height: 230px;
    border-radius: 50%;
    background: var(--ice);
    opacity: 0.8;
  }
  .brand {
    position: absolute;
    left: 38px; top: 78px;
  }
  .brand__row { display: flex; align-items: center; gap: 12px; }
  .brand__dot {
    width: 30px; height: 30px;
    border-radius: 50%;
    background: var(--sky);
  }
  .brand__name {
    font-weight: 800;
    font-size: 46px;
    letter-spacing: 0.5px;
    color: var(--navy);
    line-height: 1;
  }
  .brand__services {
    margin-top: 8px;
    margin-left: 42px;
    font-size: 10px;
    font-weight: 600;
    letter-spacing: 3.2px;
    color: var(--ink);
  }
  .person {
    position: absolute;
    right: 34px; top: 64px;
    text-align: right;
  }
  .person__name {
    font-weight: 700;
    font-size: 22px;
    letter-spacing: 0.5px;
    color: var(--blue);
  }
  .person__title {
    margin-top: 4px;
    font-size: 14px;
    font-weight: 400;
    color: var(--grey);
  }
  .contact {
    position: absolute;
    left: 80px; bottom: 40px;
    list-style: none;
    display: flex; flex-direction: column; gap: 5px;
  }
  .contact__item {
    display: flex; align-items: center; gap: 10px;
    font-size: 13px;
    color: var(--grey);
  }
  .contact__item--phone { font-size: 15px; font-weight: 500; color: var(--ink); }
  .contact__icon { width: 12px; height: 12px; flex: none; }

  /* Back */
  .card--back {
    background: var(--blue);
    display: flex; flex-direction: column;
    align-items: center; justify-content: center;
    gap: 26px;
  }
  .back__brand {
    display: flex; align-items: center; gap: 14px;
    margin-top: 10px;
  }
  .back__dot {
    width: 34px; height: 34px;
    border-radius: 50%;
    background: var(--white);
  }
  .back__name {
    font-weight: 800;
    font-size: 50px;
    color: var(--white);
    line-height: 1;
  }
  .back__tagline {
    font-weight: 700;
    font-size: 19px;
    letter-spacing: 1.5px;
    color: var(--white);
  }
</style>
</head>
<body>

  <section class="card card--front" aria-label="Business card front">
    <div class="card__halo"></div>
    <div class="brand">
      <div class="brand__row">
        <span class="brand__dot"></span>
        <span class="brand__name">harborline</span>
      </div>
      <p class="brand__services">PLUMBING · HEATING · GASFITTING</p>
    </div>

    <div class="person">
      <p class="person__name">DANIEL HART</p>
      <p class="person__title">Founder &amp; CEO</p>
    </div>

    <ul class="contact">
      <li class="contact__item contact__item--phone">
        <svg class="contact__icon" viewBox="0 0 24 24" fill="#0677BA"><path d="M6.6 10.8a15.1 15.1 0 0 0 6.6 6.6l2.2-2.2a1 1 0 0 1 1-.25 11.4 11.4 0 0 0 3.6.57 1 1 0 0 1 1 1V20a1 1 0 0 1-1 1A17 17 0 0 1 3 4a1 1 0 0 1 1-1h3.5a1 1 0 0 1 1 1c0 1.25.2 2.45.57 3.57a1 1 0 0 1-.25 1z"/></svg>
        (555) 218-4630
      </li>
      <li class="contact__item">
        <svg class="contact__icon" viewBox="0 0 24 24" fill="#0677BA"><path d="M2 5h20v14H2z" /><path d="M2 5l10 8 10-8" fill="none" stroke="#fff" stroke-width="2"/></svg>
        daniel@harborline.com
      </li>
      <li class="contact__item">
        <svg class="contact__icon" viewBox="0 0 24 24"><circle cx="12" cy="12" r="10" fill="#0677BA"/><path d="M2 12h20M12 2c3 3 3 17 0 20M12 2c-3 3-3 17 0 20" fill="none" stroke="#fff" stroke-width="1.6"/></svg>
        www.harborline.com
      </li>
    </ul>

    <div class="card__accent"></div>
  </section>

  <section class="card card--back" aria-label="Business card back">
    <div class="back__brand">
      <span class="back__dot"></span>
      <span class="back__name">harborline</span>
    </div>
    <p class="back__tagline">24/7 EMERGENCY SERVICE</p>
  </section>

</body>
</html>
```